Book Cover Contest: "Roads Toward Quiet Grace"

The KR Verlag Islamic Library invites designers and artists to design a cover for the upcoming book “Roads Toward Quiet Grace”.

This inspiring work is by Shaikh Yūsuf al-Karīm ibn Hāmid ibn Ubaydillah al-Mazrūʿī (d. 1376 AH/1957 CE), a renowned Islamic scholar. In his writing, he imparts timeless principles for inner peace and true happiness based on Islamic faith and spiritual knowledge.

Important details for the cover design:
The cover should reflect the theme of the book: paths to happiness, spiritual satisfaction, a fulfilled life.
It may contain both modern and traditional elements, but should be clear, appealing and reader-friendly.
The title “Roads toward quiet grace” should be clearly visible.
Author: Šaiḫ Yūsuf al-Karīm ibn Ḥāmid ibn ʿUbaydillah al-Mazrūʿī
Translation: Marlene Kürten

KR Verlag Islamic Library

Do you have a creative idea for the cover? Then join in and design the face of this inspiring work!

Target Market(s)

Islamic

Font styles to use
Decorative
Script

Requirements
Should not have
• No mosque silhouette, no hanging lamp,

```html
<!DOCTYPE html>
<html lang="de">
<head>
<meta charset="utf-8">
<title>Wege zu einer stillen Gnade</title>
<link rel="stylesheet" href="https://fonts.googleapis.com/css2?family=Playball&family=Playfair+Display:wght@700;800;900&family=Montserrat:wght@600;700&display=swap">
<style>
  :root {
    --ink-deep: #1c2a2c;
    --ink-mid: #2b3b3d;
    --glow-core: #ffd27a;
    --glow-warm: #e39a3a;
    --glow-amber: #8a5a2a;
    --text-light: #ffffff;
  }
  html, body {
    margin: 0;
    padding: 0;
    overflow: hidden;
    background: var(--ink-deep);
  }
  h1, p { margin: 0; }
  .cover {
    position: relative;
    width: 821px;
    height: 1200px;
    overflow: hidden;
    color: var(--text-light);
  }
  .cover-scene {
    position: absolute;
    inset: 0;
    background:
      radial-gradient(ellipse 150px 360px at 565px 620px, var(--glow-core) 0%, var(--glow-warm) 45%, rgba(227,154,58,0) 100%),
      radial-gradient(ellipse 330px 520px at 520px 700px, rgba(138,90,42,0.75) 0%, rgba(138,90,42,0) 100%),
      radial-gradient(ellipse 420px 260px at 300px 1080px, rgba(150,140,120,0.35) 0%, rgba(150,140,120,0) 100%),
      linear-gradient(180deg, var(--ink-mid) 0%, var(--ink-deep) 60%, #141c1d 100%);
  }
  .title-script,
  .title-main,
  .title-spaced,
  .byline {
    position: absolute;
    left: 0;
    width: 821px;
    text-align: center;
    line-height: 1;
    display: block;
  }
  .title-script {
    top: 82px;
    font-family: "Playball", cursive;
    font-size: 58px;
    font-weight: 400;
  }
  .title-main {
    top: 151px;
    font-family: "Playfair Display", serif;
    font-weight: 900;
    font-size: 82px;
    letter-spacing: 1px;
  }
  .title-spaced {
    top: 221px;
    font-family: "Playfair Display", serif;
    font-weight: 800;
    font-size: 78px;
    letter-spacing: 22px;
    padding-left: 22px;
    box-sizing: border-box;
  }
  .byline {
    font-family: "Playfair Display", serif;
    font-weight: 800;
  }
  .byline-von { top: 943px; font-size: 33px; }
  .byline-author { top: 993px; font-size: 34px; }
  .credit {
    position: absolute;
    text-align: center;
    font-family: "Montserrat", sans-serif;
    font-weight: 600;
    line-height: 1;
  }
  .credit-label { display: block; font-size: 13px; margin-bottom: 9px; }
  .credit-name { display: block; font-size: 20px; }
  .credit-editor { left: 60px; width: 280px; top: 1083px; }
  .credit-translator { left: 500px; width: 290px; top: 1083px; }
  .credit-translator .credit-label { font-weight: 700; letter-spacing: 0.5px; }
  .credit-translator .credit-name { font-weight: 700; }
  .publisher {
    position: absolute;
    left: 360px;
    width: 100px;
    top: 1054px;
    text-align: center;
    font-family: "Montserrat", sans-serif;
    font-weight: 600;
    font-size: 11px;
    line-height: 1;
  }
  .publisher-mark {
    display: block;
    width: 40px;
    height: 40px;
    margin: 0 auto 14px;
    border: 2px solid var(--text-light);
    box-sizing: border-box;
  }
</style>
</head>
<body>
  <main class="cover">
    <div class="cover-scene" role="img" aria-label="Photograph of a dim stone interior with an arched window of ornate lattice glowing golden, light rays falling onto steps in mist"></div>

    <h1>
      <span class="title-script">Wege zu einer</span>
      <span class="title-main">STILLEN</span>
      <span class="title-spaced">GNADE</span>
    </h1>

    <p class="byline byline-von">Von</p>
    <p class="byline byline-author">Šaiḫ Yūsuf al-Karīm ibn Ḥāmid</p>

    <div class="credit credit-editor">
      <span class="credit-label">Lektort:</span>
      <span class="credit-name">Dr: Tobias Amin Lehr</span>
    </div>

    <div class="publisher">
      <span class="publisher-mark"></span>
      KR Verlag
    </div>

    <div class="credit credit-translator">
      <span class="credit-label">ÜBERSETZUNG:</span>
      <span class="credit-name">MARLENE KÜRTEN</span>
    </div>
  </main>
</body>
</html>
```